Meadow Warden Lawn Spraying Looking for catchy Truck wrap

We are a lawn spraying company looking for a catchy truck wrap. We spray for weeds in the yard and also spray for mosquitos. We use black trucks. We want to see a modern truck wrap that uses the colors of our logo

405-555-0183
#274638 (put in smaller font on wrap somewhere. Doesn't have to be big but has to be on the truck somewhere)

Target Market(s)

All homeowners & building owners with a lawn

Industry/Entity Type

Lawn Care

Requirements
Must have
• Use the colors of the logo.
Nice to have
• Be creative with some blades of grass in the design

```html
<!DOCTYPE html>
<html lang="en">
<head>
<meta charset="utf-8">
<title>Meadow Warden Lawn Spraying — Truck Wrap</title>
<link href="https://fonts.googleapis.com/css2?family=Roboto+Condensed:wght@600;700&display=swap" rel="stylesheet">
<style>
  :root {
    --bg: #eceeef;
    --body-black: #16191b;
    --glass: #9aa7ad;
    --window-white: #e3e8f0;
    --green: #2fae2a;
    --green-light: #4fd33c;
    --green-dark: #1c8a1e;
    --gold: #b99a3c;
    --gold-light: #e0c86a;
    --gold-dark: #7f6a25;
    --tyre: #1e1f21;
    --rim: #b8bcbf;
    --text-white: #ffffff;
    --text-green: #5de04a;
  }
  html, body { margin: 0; padding: 0; overflow: hidden; }
  body { width: 1076px; height: 1200px; background: var(--bg); }
  .wrap-sheet { display: block; width: 1076px; height: 1200px; }
  .wrap-text { font-family: "Roboto Condensed", sans-serif; }
  .phone { font-size: 29px; font-weight: 700; fill: var(--text-green); }
  .brand-name { font-size: 38px; font-weight: 700; fill: var(--text-green); }
  .service-line { font-size: 13.5px; font-weight: 600; fill: var(--text-white); }
  .unit-number { font-size: 15px; font-weight: 700; fill: var(--text-white); }
</style>
</head>
<body>
<svg class="wrap-sheet" viewBox="0 0 1076 1200" xmlns="http://www.w3.org/2000/svg">
  <defs>
    <linearGradient id="greenPanel" x1="0" y1="0" x2="1" y2="0">
      <stop offset="0" stop-color="var(--green-dark)"/>
      <stop offset="0.5" stop-color="var(--green-light)"/>
      <stop offset="1" stop-color="var(--green)"/>
    </linearGradient>
    <linearGradient id="goldBand" x1="0" y1="0" x2="1" y2="0">
      <stop offset="0" stop-color="var(--gold-dark)"/>
      <stop offset="0.45" stop-color="var(--gold-light)"/>
      <stop offset="1" stop-color="var(--gold)"/>
    </linearGradient>
    <linearGradient id="grassStrip" x1="0" y1="0" x2="0" y2="1">
      <stop offset="0" stop-color="var(--green-dark)" stop-opacity="0.2"/>
      <stop offset="0.5" stop-color="var(--green)"/>
      <stop offset="1" stop-color="var(--green-light)"/>
    </linearGradient>

    <g id="truckSide">
      <!-- black body -->
      <path class="truck-body" fill="var(--body-black)"
        d="M78 265 L150 218 L430 200 L560 108 L960 90 Q990 92 992 120 L992 400 Q990 414 975 414 L410 414 Q400 345 320 338 Q240 338 220 402 L135 402 L78 380 Z"/>
      <!-- cab door window -->
      <path class="door-window" fill="var(--glass)" d="M478 120 L735 112 L740 212 L478 222 Z"/>
      <!-- rear green panel -->
      <path class="rear-panel" fill="url(#greenPanel)" d="M745 92 L960 90 Q990 92 992 120 L992 400 Q990 414 975 414 L745 414 Z"/>
      <!-- rear window -->
      <rect class="rear-window" x="772" y="110" width="156" height="102" rx="10" fill="var(--window-white)"/>
      <!-- gold swoosh -->
      <path class="gold-band" fill="url(#goldBand)"
        d="M742 92 L770 92 Q790 200 820 212 L960 218 Q880 230 850 262 Q820 300 822 414 L420 414 Q520 392 700 356 Q738 340 742 300 Z"/>
      <!-- black door panel with curved trailing edge -->
      <path class="door-panel" fill="var(--body-black)"
        d="M470 222 L740 212 L742 300 Q738 340 700 350 Q560 362 420 370 L420 240 Z"/>
      <!-- grass strip -->
      <g role="img" aria-label="Blades of grass growing along the lower door">
        <path fill="url(#grassStrip)" d="M420 350 Q560 346 700 350 Q600 380 420 414 Z"/>
      </g>
      <!-- wheel -->
      <circle class="tyre" cx="316" cy="462" r="90" fill="var(--tyre)"/>
      <circle class="rim" cx="316" cy="462" r="52" fill="var(--rim)"/>
      <circle cx="316" cy="462" r="16" fill="#8c9094"/>
      <!-- running board -->
      <rect x="480" y="428" width="480" height="12" rx="4" fill="var(--body-black)"/>
    </g>
  </defs>

  <!-- driver side (facing left) -->
  <g class="truck-view truck-view--driver">
    <use href="#truckSide"/>
    <g class="wrap-text">
      <text class="phone" x="252" y="274">405-555-0183</text>
      <text class="brand-name" x="486" y="296">Meadow</text>
      <text class="brand-name" x="486" y="336">Warden</text>
      <text class="service-line" x="855" y="304">Spray for weeds &amp;</text>
      <text class="service-line" x="855" y="320">Spray for mosquitos</text>
      <text class="service-line" x="855" y="336">Control</text>
      <text class="unit-number" x="860" y="384">#274638</text>
    </g>
  </g>

  <!-- passenger side (facing right) -->
  <g class="truck-view truck-view--passenger" transform="translate(0 590)">
    <use href="#truckSide" transform="translate(1076 0) scale(-1 1)"/>
    <g class="wrap-text">
      <text class="phone" x="824" y="274" text-anchor="end">405-555-0183</text>
      <text class="brand-name" x="392" y="296">Meadow</text>
      <text class="brand-name" x="392" y="336">Warden</text>
      <text class="service-line" x="216" y="304" text-anchor="end">Spray for weeds &amp;</text>
      <text class="service-line" x="216" y="320" text-anchor="end">Spray for mosquitos</text>
      <text class="service-line" x="216" y="336" text-anchor="end">Control</text>
      <text class="unit-number" x="216" y="384" text-anchor="end">#274638</text>
    </g>
  </g>
</svg>
</body>
</html>
```